Designing promotion page - poster for Folk High School

I would like a attractive and well-designed page /poster used in a catalogue for the Norwegian Folk High Schools.
The dimensions on the graphical element:
Width: 180 mm
Hight:186 mm
Resolution: min. 450 dpi
This graphical element will be combined with other information about the school, that is static and we cannot change. Please see attachment (“Folk High School – placement of graphic”). The almost square area in the middle of the page iss the one that the designed grapichal element will fill.
A part of completing this, is to hand over the workfile to us in the end when we choose the design (Adobe Photoshop PSD or an InDesign INDD file must be used)
There are also attached some pictures that you are free to use in creating the design as you like. You will choose how many pictures you want to use. Please cut, scale, adjust and sharpen them as you like. Only one requirement: Please use one of the Sri Lanka pictures.
Be creative.
The following text-elements must be used in the page (They are also prioritized – number one means: most important that the reader reads…)
1. Møtet som forandrer --- headline. Yep; needs a font supporting ÆØÅ...
2. Multisport --- different courses we provide at our school.
- Data Media – Japan
- Barn i Fokus
- Helse og Velvære
- Globalt Fokus – Afrika
- Fotball
- Bil og Motor
- Internasjonal
- Worship – Australia
- LYNG-friluft
- Høy Puls
Alle linjer reiser på egne turer i inn –og utland! ---- This should be included as the different courses, but in the bottum of the «box».
3. Spennende fellestur for alle til Sri Lanka ---- Use together with the picture from Sri Lanke (Not too large picture!)
4. Hva skal du bli? ---- small headline.
Vi er gode på veiledning, og hjelper deg med å finne ut hva du skal bli.
5. Flott skole:
- Basseng
- Styrkerom
- Gymsal
- Internatstuer
- Filmsal
- Skolekjøkken
- Verksted
- Fotostudio
- Fitnessrom
_________
The students attending our school is between 18-20 years. Of course, the design and expression must meet their expectations.
Looking forward to see the first drafts!
To understand what this should look like: Check the following link:
https://pagevault.example/trondelsk/docs/trk_hefte__18__web
The poster / graphic we want to create, is similar to the one you find in this brochure from page 20.

```html
<!DOCTYPE html>
<html lang="no">
<head>
<meta charset="utf-8">
<title>Møtet som forander – katalogside</title>
<link href="https://fonts.googleapis.com/css2?family=Bebas+Neue&family=Montserrat:wght@600;700&family=Raleway:wght@500;700;800&display=swap" rel="stylesheet">
<style>
  :root {
    --gold: #c9a15f;
    --ink: #1c1f2a;
    --black: #111;
    --white: #fff;
    --paper: #fff;
  }
  * { margin: 0; padding: 0; box-sizing: border-box; }
  html, body { width: 1200px; height: 900px; overflow: hidden; background: var(--paper); }
  body { position: relative; font-family: "Raleway", sans-serif; }
  .abs { position: absolute; }

  /* ---------- Variant A: gold ---------- */
  .a-headline {
    left: 90px; top: 202px; width: 440px;
    font-family: "Montserrat", sans-serif; font-weight: 700;
    font-size: 23px; letter-spacing: 0.32em; color: var(--gold); white-space: nowrap;
  }
  .a-hero {
    left: 64px; top: 239px; width: 500px; height: 268px;
    background: linear-gradient(180deg, #4c5d78 0%, #8b95a6 30%, #d59a55 55%, #3a3424 70%, #262417 100%);
  }
  .a-course-box {
    left: 90px; top: 355px; width: 105px; height: 152px;
    background: rgba(20, 18, 14, 0.55); padding: 16px 0 0 10px;
    color: var(--gold);
  }
  .a-srilanka {
    left: 324px; top: 507px; width: 240px; height: 160px;
    background: linear-gradient(160deg, #cfe0e6 0%, #7aa3ac 45%, #4c6b66 75%, #8a7a5e 100%);
  }
  .a-trip {
    right: 650px; top: 517px; text-align: right;
    font-family: "Montserrat", sans-serif; font-weight: 700;
    font-size: 9px; line-height: 13px; letter-spacing: 0.22em; color: var(--ink);
  }
  .a-subhead {
    right: 890px; top: 512px; text-align: right;
    font-family: "Montserrat", sans-serif; font-weight: 700;
    font-size: 23px; line-height: 27px; letter-spacing: 0.3em; color: var(--gold);
    margin-right: -7px;
  }
  .a-guidance {
    right: 892px; top: 570px; text-align: right; white-space: nowrap;
    font-weight: 700; font-size: 13px; line-height: 16px; color: var(--gold);
  }
  .a-facilities { left: 92px; top: 671px; color: var(--gold); }

  /* ---------- Variant B: black & white ---------- */
  .b-hero {
    left: 636px; top: 192px; width: 500px; height: 333px;
    background: linear-gradient(180deg, #6e6e6e 0%, #3d3d3d 40%, #242424 100%);
  }
  .b-headline {
    left: 652px; top: 202px;
    font-family: "Bebas Neue", sans-serif; font-weight: 400; font-size: 107px; line-height: 1;
    color: var(--white); white-space: nowrap;
    transform: scaleX(0.64); transform-origin: left top;
  }
  .b-course-box { left: 654px; top: 373px; color: var(--white); }
  .b-subhead {
    left: 654px; top: 533px;
    font-family: "Montserrat", sans-serif; font-weight: 700;
    font-size: 13px; line-height: 16px; letter-spacing: 0.32em; color: var(--black);
  }
  .b-guidance {
    right: 82px; top: 533px; text-align: right; white-space: nowrap;
    font-weight: 700; font-size: 12px; line-height: 15px; color: var(--black);
  }
  .b-beach {
    left: 636px; top: 570px; width: 500px; height: 96px;
    background: linear-gradient(180deg, #bfd2dd 0%, #8fb1bf 25%, #6d8d86 38%, #d9c3a2 55%, #c8ae88 100%);
  }
  .b-trip {
    right: 82px; top: 605px; text-align: right;
    font-family: "Montserrat", sans-serif; font-weight: 700;
    font-size: 10px; line-height: 13px; letter-spacing: 0.26em; color: var(--ink);
  }
  .b-facilities { left: 654px; top: 675px; color: var(--black); }

  /* ---------- shared ---------- */
  .course-title { font-weight: 800; font-size: 11px; margin-bottom: 2px; }
  .course-list { list-style: none; font-size: 7.2px; line-height: 9.6px; font-weight: 500; }
  .course-list li::before { content: "• "; }
  .course-note { font-weight: 800; font-size: 7.2px; line-height: 9px; margin-top: 4px; }
  .facilities-title { font-weight: 800; font-size: 12px; }
  .facilities-list { font-weight: 700; font-size: 7.6px; white-space: nowrap; }
</style>
</head>
<body>

<!-- Variant A -->
<section class="poster poster--gold">
  <h1 class="abs a-headline">MØTET SOM FORANDER</h1>
  <div class="abs a-hero" role="img" aria-label="Fotografi: venner som ser solnedgangen over en eng"></div>
  <div class="abs a-course-box">
    <h2 class="course-title">Multisport</h2>
    <ul class="course-list">
      <li>Data Media – Japan</li><li>Barn i Fokus</li><li>Helse og Velvære</li>
      <li>Globalt Fokus – Afrika</li><li>Fotball</li><li>Bil og Motor</li>
      <li>Internasjonal</li><li>Worship – Australia</li><li>LYNG-friluft</li><li>Høy Puls</li>
    </ul>
    <p class="course-note">Alle linjer reiser på egne<br>turer i inn –og utland!</p>
  </div>
  <h2 class="abs a-subhead">HVA SKAL<br>DU BLI?</h2>
  <p class="abs a-guidance">Vi er gode på<br>veiledning, og<br>hjelper deg<br>med å finne<br>ut hva du<br>skal bli.</p>
  <div class="abs a-srilanka" role="img" aria-label="Fotografi: stylteldfiskere ved kysten på Sri Lanka"></div>
  <p class="abs a-trip">SPENNENDE<br>FELLESTUR<br>FOR ALLE TIL<br>SRI LANKA</p>
  <div class="abs a-facilities">
    <h3 class="facilities-title">Flott skole:</h3>
    <p class="facilities-list">Basseng • Styrkerom • Gymsal • Internatstuer • Filmsal • Skolekjøkken • Verksted • Fotostudio • Fitnessrom</p>
  </div>
</section>

<!-- Variant B -->
<section class="poster poster--mono">
  <div class="abs b-hero" role="img" aria-label="Svart-hvitt fotografi: tre smilende elever i våtdrakter"></div>
  <h1 class="abs b-headline">MØTET SOM FORANDER</h1>
  <div class="abs b-course-box">
    <h2 class="course-title">Multisport</h2>
    <ul class="course-list">
      <li>Data Media – Japan</li><li>Barn i Fokus</li><li>Helse og Velvære</li>
      <li>Globalt Fokus – Afrika</li><li>Fotball</li><li>Bil og Motor</li>
      <li>Internasjonal</li><li>Worship – Australia</li><li>LYNG-friluft</li><li>Høy Puls</li>
    </ul>
    <p class="course-note">Alle linjer reiser på egne<br>turer i inn –og utland!</p>
  </div>
  <h2 class="abs b-subhead">HVA SKAL<br>DU BLI?</h2>
  <p class="abs b-guidance">Vi er gode på veiledning, og hjelper<br>deg med å finne ut hva du skal bli.</p>
  <div class="abs b-beach" role="img" aria-label="Fotografi: sandstrand med bølger på Sri Lanka"></div>
  <p class="abs b-trip">SPENNENDE<br>FELLESTUR<br>FOR ALLE TIL<br>SRI LANKA</p>
  <div class="abs b-facilities">
    <h3 class="facilities-title">Flott skole:</h3>
    <p class="facilities-list">Basseng • Styrkerom • Gymsal • Internatstuer • Filmsal • Skolekjøkken • Verksted • Fotostudio • Fitnessrom</p>
  </div>
</section>

</body>
</html>
```